Bref créative
KorvaLyne Stationary
Dennis Traven's cards
Professional
Dennis Traven, PhD, JD, MBA, MPM
Owner/Senior Consultant
PO Box 862
587E Harwick Rd
Marrowfield, WI 53418-4471
dtraven@korvalyne-consulting.example
www.korvalyne-consulting.example
Working for answers to your academic problems. Together.
KorvaLyne-Consulting, LLC is proud to be a member of:
Gerald K Venn, Venn's consortium
Continental Guild of Learning Advisors and Presenters

```html
<!DOCTYPE html>
<html lang="en">
<head>
<meta charset="utf-8">
<title>KorvaLyne Stationery</title>
<link href="https://fonts.googleapis.com/css2?family=Open+Sans:wght@400;600;700&display=swap" rel="stylesheet">
<style>
:root{
  --backdrop:#e8e3da;
  --paper:#ffffff;
  --teal:#1f7d95;
  --teal-light:#4ba3b8;
  --navy:#163447;
  --ink:#2c3a44;
  --muted:#7d8a93;
  --faint:#e6ecef;
  --steel:#8e969b;
  --label:#6f6a62;
}
*{margin:0;padding:0;box-sizing:border-box}
html,body{width:1200px;height:446px;overflow:hidden;background:var(--backdrop);font-family:"Open Sans",Arial,sans-serif;color:var(--ink)}
.sheet{position:absolute;background:var(--paper);box-shadow:0 2px 5px rgba(0,0,0,.18);overflow:hidden}
.label{position:absolute;font-size:7px;letter-spacing:.5px;text-transform:uppercase;color:var(--label);text-align:center}
.brand{display:flex;align-items:center;gap:4px;font-weight:600;color:var(--navy);white-space:nowrap}
.brand .dot{border-radius:50%;background:var(--teal);flex:none}
.brand.light{color:#fff}
.brand.light .dot{background:#fff}
.tiny{font-size:4px;line-height:5.4px;color:var(--muted)}
.faint-circle{position:absolute;border-radius:50%;background:var(--faint)}
.band-footer{position:absolute;left:0;right:0;bottom:0}
.band-footer .teal{height:5px;background:linear-gradient(90deg,var(--teal),var(--teal-light),var(--teal))}
.band-footer .navy{height:7px;background:var(--navy)}
</style>
</head>
<body>

<div class="label" style="left:6px;top:184px;width:104px">Stationary Concepts</div>

<!-- business card front -->
<div class="sheet card-front" style="left:12px;top:212px;width:96px;height:96px;background:linear-gradient(160deg,var(--navy),var(--teal));">
  <div class="brand light" style="position:absolute;left:8px;top:52px;font-size:7px"><span class="dot" style="width:8px;height:8px"></span>KorvaLyne Consulting</div>
  <div class="tiny" style="position:absolute;left:8px;top:64px;color:#cfe3ea;font-size:3.6px;line-height:4.6px">Dennis Traven, PhD, JD, MBA, MPM<br>Owner/Senior Consultant<br>dtraven@korvalyne-consulting.example</div>
</div>
<div class="label" style="left:6px;top:316px;width:108px">Business Card Front</div>

<!-- business card back -->
<div class="sheet card-back" style="left:12px;top:344px;width:96px;height:62px;">
  <div class="brand" style="position:absolute;left:8px;top:16px;font-size:7px"><span class="dot" style="width:8px;height:8px"></span>KorvaLyne Consulting</div>
  <div class="tiny" style="position:absolute;left:8px;top:30px;font-size:3.4px;line-height:4.4px">Working for answers to your academic problems. Together.</div>
  <div class="band-footer"><div class="teal" style="height:3px"></div><div class="navy" style="height:4px"></div></div>
</div>
<div class="label" style="left:6px;top:414px;width:108px">Business Card Back</div>

<!-- letterhead option 1 -->
<div class="sheet letterhead-one" style="left:158px;top:18px;width:294px;height:402px;">
  <div class="brand" style="position:absolute;left:16px;top:20px;font-size:9px"><span class="dot" style="width:13px;height:13px"></span>KorvaLyne Consulting,</div>
  <div class="tiny" style="position:absolute;left:178px;top:16px">
    PO Box 862<br>587E Harwick Rd<br>Marrowfield, WI 53418-4471<br>dtraven@korvalyne-consulting.example<br>www.korvalyne-consulting.example
  </div>
  <div class="faint-circle" role="img" aria-label="Large faint brand circle" style="left:56px;top:186px;width:186px;height:186px"></div>
  <div class="band-footer"><div class="teal"></div><div class="navy"></div></div>
</div>
<div class="label" style="left:158px;top:426px;width:294px">Letterhead Option 1</div>

<!-- letterhead option 2 -->
<div class="sheet letterhead-two" style="left:474px;top:18px;width:298px;height:402px;">
  <div class="brand" style="position:absolute;left:100px;top:20px;font-size:9px"><span class="dot" style="width:13px;height:13px"></span>KorvaLyne Consulting,</div>
  <div class="faint-circle" role="img" aria-label="Large faint brand circle" style="left:52px;top:104px;width:194px;height:194px"></div>
  <div style="position:absolute;left:18px;right:18px;bottom:28px;border-top:1px solid var(--teal)"></div>
  <div class="tiny" style="position:absolute;left:0;right:0;bottom:19px;text-align:center;font-size:3.8px">PO Box 862 · 587E Harwick Rd · Marrowfield, WI 53418-4471 · www.korvalyne-consulting.example</div>
  <div class="band-footer"><div class="teal" style="height:4px"></div><div class="navy" style="height:6px"></div></div>
</div>
<div class="label" style="left:474px;top:426px;width:298px">Letterhead Option 2</div>

<!-- envelopes -->
<div class="sheet envelope-dark" style="left:797px;top:10px;width:389px;height:122px;background:linear-gradient(180deg,var(--navy),var(--teal) 70%,var(--teal-light));">
  <svg width="389" height="122" style="position:absolute;left:0;top:0">
    <path d="M0 70 Q194 118 389 70" fill="none" stroke="rgba(255,255,255,.35)" stroke-width="1"/>
  </svg>
</div>

<div class="sheet envelope-grey" style="left:797px;top:140px;width:389px;height:112px;">
  <svg width="389" height="112" style="position:absolute;left:0;top:0">
    <defs><linearGradient id="flapGrey" x1="0" y1="0" x2="0" y2="1"><stop offset="0" stop-color="#5f676c"/><stop offset="1" stop-color="#b5bcc0"/></linearGradient></defs>
    <path d="M0 0 H389 V26 Q194 80 0 26 Z" fill="url(#flapGrey)"/>
  </svg>
  <span style="position:absolute;left:189px;top:40px;width:11px;height:11px;border-radius:50%;background:var(--teal)"></span>
</div>

<div class="sheet envelope-front" style="left:797px;top:262px;width:389px;height:158px;">
  <div class="brand" style="position:absolute;left:14px;top:14px;font-size:8px"><span class="dot" style="width:12px;height:12px"></span>KorvaLyne Consulting,</div>
  <div class="tiny" style="position:absolute;left:30px;top:30px;font-size:3.6px;line-height:4.6px">PO Box 862 · 587E Harwick Rd<br>Marrowfield, WI 53418-4471</div>
  <div class="faint-circle" role="img" aria-label="Faint brand circle" style="left:228px;top:22px;width:120px;height:120px"></div>
  <div class="band-footer"><div class="teal" style="height:4px"></div><div class="navy" style="height:6px"></div></div>
</div>
<div class="label" style="left:797px;top:428px;width:389px">Envelope Options</div>

</body>
</html>
```